Kelvorn LLC web design project

Dallas, TX based water damage mitigation company needs a web site for its new business. The company does water extractions, mitigation, demo, restoration, and reconstruction. We need for the site to have a strong mobile version, and the owners/managers need to be able to edit the site despite having no web design experience. The site needs to look and function, especially the mobile version, similar to marbleforkquiltshop.com if possible.

```html
<!DOCTYPE html>
<html lang="en">
<head>
<meta charset="utf-8">
<title>Kelvorn LLC — Water Damage Mitigation</title>
<link href="https://fonts.googleapis.com/css2?family=Montserrat:wght@400;500;700;800;900&family=Roboto:ital,wght@0,400;0,500;0,700;1,400&display=swap" rel="stylesheet">
<style>
:root{
  --blue:#0b4bb3;
  --blue-bright:#1556c9;
  --navy:#1c2b4a;
  --navy-deep:#18233a;
  --ink:#222;
  --muted:#666;
  --white:#fff;
  --footer:#1d222b;
  --gold:#f3c21b;
}
*{box-sizing:border-box;margin:0;padding:0}
html,body{width:1200px;height:4292px;overflow:hidden}
body{position:relative;font-family:'Roboto',sans-serif;color:var(--ink);background:var(--white)}
.abs{position:absolute}
h2.section-title{position:absolute;left:0;width:1200px;text-align:center;font-family:'Montserrat',sans-serif;font-size:44px;font-weight:400;color:var(--blue);letter-spacing:.5px}
h2.section-title b{font-weight:900}
.btn{position:absolute;display:flex;align-items:center;justify-content:center;border-radius:30px;font-family:'Roboto',sans-serif;font-weight:500;font-size:14px;color:var(--white);text-transform:uppercase}
.btn-navy{background:var(--navy)}
.btn-blue{background:var(--blue-bright)}

/* hero */
.hero-photo{left:0;top:0;width:1200px;height:720px;background:linear-gradient(180deg,#7fa6d6 0%,#4b6fa4 25%,#34425e 48%,#5a4a4a 58%,#2e3d57 72%,#1f2a3c 100%)}
.brand{left:145px;top:95px;width:190px;text-align:center;font-family:'Montserrat',sans-serif;font-weight:800;font-size:34px;color:var(--navy);letter-spacing:1px}
.brand small{display:block;font-size:13px;letter-spacing:6px;font-weight:800;margin-top:2px}
.phone-pill{left:667px;top:55px;width:258px;height:62px;border-radius:31px;background:var(--blue-bright);border:3px solid #fff;display:flex;align-items:center;gap:14px;padding-left:8px;color:#fff;font-weight:700;font-size:20px}
.phone-pill .ico{width:40px;height:40px;border-radius:50%;background:#fff;display:flex;align-items:center;justify-content:center}
.menu{left:963px;top:74px;display:flex;align-items:center;gap:18px;font-size:17px;font-weight:500;color:var(--navy)}
.hero-title{left:0;top:285px;width:1200px;text-align:center;font-family:'Montserrat',sans-serif;font-weight:900;font-size:76px;line-height:76px;color:#fff;text-shadow:3px 3px 0 rgba(20,30,60,.9)}
.hero-title span{font-weight:500}
.dots{left:563px;top:580px;display:flex;gap:8px}
.dots i{width:12px;height:12px;border-radius:50%;background:#fff}
.dots i.on{background:var(--blue-bright)}

/* services */
.services-bg{left:0;top:773px;width:1200px;height:700px;background:linear-gradient(180deg,#eef1f5 0%,#f6f7f9 70%,#fff 100%)}
.card{position:absolute;top:892px;width:217px;height:495px;background:#fff;border:1px solid #d6d9de}
.card .photo{position:absolute;left:7px;top:8px;width:203px;height:142px}
.card .label{position:absolute;left:7px;top:150px;width:203px;height:42px;background:var(--blue-bright);border-radius:0 0 18px 18px;color:#fff;font-size:15px;font-weight:500;display:flex;align-items:center;justify-content:center}
.card p{position:absolute;left:14px;top:222px;width:189px;font-size:12.5px;line-height:22.5px;color:var(--muted);text-align:center}
.card .btn{left:33px;top:420px;width:150px;height:50px}
.arrow{position:absolute;width:44px;height:44px;border-radius:50%;border:1.5px solid #666;background:rgba(255,255,255,.7);display:flex;align-items:center;justify-content:center}

/* about */
.about-panel{left:-10px;top:1478px;width:1065px;height:500px;background:var(--blue);border-radius:0 250px 250px 0}
.about-title{left:145px;top:1560px;font-family:'Montserrat',sans-serif;font-size:46px;color:#fff;font-weight:500}
.about-title b{font-weight:900}
.about-text{left:145px;top:1642px;width:440px;font-size:12.5px;line-height:22.5px;color:#fff}

/* pricing */
.feature{position:absolute;width:330px}
.feature .ico{position:absolute;top:0;width:70px;height:70px;border-radius:50%;display:flex;align-items:center;justify-content:center}
.feature h3{position:absolute;top:0;font-size:17px;font-weight:700;color:#222;white-space:nowrap}
.feature p{position:absolute;top:32px;width:215px;font-size:13.5px;line-height:25px;color:var(--muted)}
.feature.left .ico{left:0}
.feature.left h3,.feature.left p{left:85px}
.feature.right .ico{right:0}
.feature.right h3,.feature.right p{right:85px;text-align:right}
.ico-navy{background:var(--navy)}
.ico-blue{background:var(--blue-bright)}
.price-photo{left:455px;top:2243px;width:290px;height:290px;border-radius:50%;border:4px solid #fff;box-shadow:0 4px 14px rgba(0,0,0,.35);background:radial-gradient(circle at 40% 35%,#d9c4a0 0%,#b89a74 45%,#e86a1c 75%,#c9b08e 100%)}

/* cta */
.cta-panel{left:147px;top:2672px;width:1060px;height:498px;border-radius:249px 0 0 249px;background:linear-gradient(90deg,#1f2f55 0%,#243866 60%,#2b3f6a 100%)}
.cta-title{left:300px;top:2790px;width:760px;text-align:center;font-family:'Montserrat',sans-serif;font-weight:900;font-size:44px;line-height:54px;color:#fff}

/* reviews */
.reviews-bg{left:0;top:3170px;width:1200px;height:720px;background:linear-gradient(180deg,#f7f8fa 0%,#eceef2 55%,#dfe3ea 100%)}
.review{position:absolute;top:3408px;width:305px}
.review .avatar{position:absolute;left:0;top:0;width:66px;height:66px;border-radius:50%;border:3px solid #fff;background:radial-gradient(circle,#c9a78e 0%,#8a6b58 100%);box-shadow:0 1px 4px rgba(0,0,0,.3)}
.review q{position:absolute;left:85px;top:2px;width:215px;font-style:italic;font-size:11px;line-height:22px;color:#888;quotes:none}
.review q::before{content:"\201C";font-size:24px;font-weight:700;color:#333;font-style:italic;margin-right:6px;vertical-align:-7px}
.review .who{position:absolute;left:85px;top:84px;font-size:9.5px;line-height:18px;color:#333}
.review .who i{display:block;font-size:9px}
.review .stars{position:absolute;left:85px;top:132px;display:flex;gap:4px}

/* footer */
.footer{left:0;top:3840px;width:1200px;height:452px;background:var(--footer)}
.contact{position:absolute;left:150px;display:flex;align-items:center;gap:16px;color:#fff;font-size:13px;line-height:22px}
.contact .ico{width:42px;height:42px;border-radius:50%;border:1.5px solid #fff;display:flex;align-items:center;justify-content:center;flex:none}
.contact .ico.fill{background:var(--blue-bright);border-color:var(--blue-bright)}
.links{left:538px;top:3955px;color:#fff}
.links h4{font-size:19px;font-weight:500;margin-bottom:22px}
.links li{list-style:none;font-size:13px;line-height:22.5px}
.footer-brand{left:783px;top:3985px;width:270px;text-align:center;font-family:'Montserrat',sans-serif;font-weight:800;font-size:42px;color:#fff;letter-spacing:1px}
.footer-brand small{display:block;font-size:16px;letter-spacing:9px;margin-top:4px}
.legal{left:0;top:4233px;width:1200px;text-align:center;color:#fff;font-size:13px}
</style>
</head>
<body>

<!-- HERO -->
<div class="abs hero-photo" role="img" aria-label="Night skyline of a city reflected in a river"></div>
<svg class="abs" style="left:0;top:560px" width="1200" height="220" viewBox="0 0 1200 220">
  <path d="M0 95 C180 170 360 170 520 125 C700 70 900 40 1200 85 L1200 220 L0 220Z" fill="#fff"/>
  <path d="M0 95 C180 170 360 170 520 125 C700 70 900 40 1200 85 L1200 100 C900 60 700 85 520 140 C360 185 180 185 0 110Z" fill="#1c2b4a"/>
</svg>
<div class="abs brand">KELVORN<small>LLC</small></div>
<div class="abs phone-pill"><span class="ico"><svg width="22" height="22" viewBox="0 0 24 24"><path fill="#1556c9" d="M6.6 10.8a15.1 15.1 0 0 0 6.6 6.6l2.2-2.2c.3-.3.7-.4 1-.2 1.1.4 2.3.6 3.6.6.6 0 1 .4 1 1V20c0 .6-.4 1-1 1A17 17 0 0 1 3 4c0-.6.4-1 1-1h3.5c.6 0 1 .4 1 1 0 1.3.2 2.5.6 3.6.1.3 0 .7-.2 1z"/></svg></span>+1 888 888 8888</div>
<div class="abs menu"><svg width="22" height="18" viewBox="0 0 22 18"><rect width="22" height="3" fill="#1c2b4a"/><rect y="7.5" width="22" height="3" fill="#1c2b4a"/><rect y="15" width="22" height="3" fill="#1c2b4a"/></svg>MENU</div>
<h1 class="abs hero-title">WATER DAMAGE<br><span>MITIGATION</span></h1>
<div class="abs dots"><i></i><i></i><i class="on"></i><i></i></div>

<!-- SERVICES -->
<div class="abs services-bg" role="img" aria-label="Faded bright bathroom interior background"></div>
<h2 class="section-title" style="top:785px"><b>OUR</b> SERVICES</h2>
<div class="arrow" style="left:73px;top:1118px"><svg width="14" height="14" viewBox="0 0 14 14"><path d="M9 2 4 7l5 5" stroke="#444" stroke-width="2" fill="none"/></svg></div>
<div class="arrow" style="left:1083px;top:1118px"><svg width="14" height="14" viewBox="0 0 14 14"><path d="M5 2l5 5-5 5" stroke="#444" stroke-width="2" fill="none"/></svg></div>

<div class="card" style="left:145px">
  <div class="photo" role="img" aria-label="Coastline with bridge and wet shore" style="background:linear-gradient(180deg,#6f9fd6 0%,#a9c4e0 45%,#8a7c6c 70%,#5d5246 100%)"></div>
  <div class="label">WATER EXTRACTIONS</div>
  <p>Lorem ipsum dolor sit amet, consectetur adipiscing elit, sed do eiusmod tempor incididunt ut labore et dolore magna aliqua. uis ipsum suspendisse ultricesvidasummodiverraa ecena sccumsacus velf msacacilisis.</p>
  <a class="btn btn-navy">Read More</a>
</div>
<div class="card" style="left:376px">
  <div class="photo" role="img" aria-label="Worker removing flooded debris" style="background:linear-gradient(180deg,#3b4350 0%,#8d8a84 45%,#b9b5ae 70%,#6d6a66 100%)"></div>
  <div class="label">MITIGATION</div>
  <p>Lorem ipsum dolor sit amet, consectetur adipiscing elit, sed do eiusmod tempor incididunt ut labore et dolore magna aliqua. uis ipsum suspendisse ultricesvidasummodiverraa ecena sccumsacus velf msacacilisis.</p>
  <a class="btn btn-navy">Read More</a>
</div>
<div class="card" style="left:607px">
  <div class="photo" role="img" aria-label="Clear water flowing past a stone wall" style="background:linear-gradient(135deg,#e6edf2 0%,#9fb8cc 35%,#2d7fb8 65%,#1b5a8e 100%)"></div>
  <div class="label">DEMO</div>
  <p>Lorem ipsum dolor sit amet, consectetur adipiscing elit, sed do eiusmod tempor incididunt ut labore et dolore magna aliqua. uis ipsum suspendisse ultricesvidasummodiverraa ecena sccumsacus velf msacacilisis.</p>
  <a class="btn btn-navy">Read More</a>
</div>
<div class="card" style="left:837px">
  <div class="photo" role="img" aria-label="Canal lock with green banks" style="background:linear-gradient(180deg,#c6d4e4 0%,#9fb0c2 35%,#5d7a4a 55%,#4f6d7f 80%,#3e5766 100%)"></div>
  <div class="label">RESTORATION</div>
  <p>Lorem ipsum dolor sit amet, consectetur adipiscing elit, sed do eiusmod tempor incididunt ut labore et dolore magna aliqua. uis ipsum suspendisse ultricesvidasummodiverraa ecena sccumsacus velf msacacilisis.</p>
  <a class="btn btn-navy">Read More</a>
</div>

<!-- ABOUT -->
<div class="abs about-panel"></div>
<h2 class="abs about-title"><b>ABOUT</b> US</h2>
<p class="abs about-text">Lorem ipsum dolor sit amet, consectetur adipiscing elit, sed do eiusmod tempor incididunt ut labore et dolore magna aliqus ipsum suspendisse ultrices gravidsus commodo viverra maecenas accumsan lacus vel facilisis.Lorem ipsum dolor sit amet, consectetur adipiscing elit, sed do eiusmod tempor incididunt ut labore et dolore magna aliqus ipsum suspendis graviommodo viverra maecenas accumsan lacus vel facilisislorem ipsum dolor sit amet, consectetur adipiscing elit, sed do eiusmod tempor incididunt</p>
<a class="btn btn-navy" style="left:145px;top:1833px;width:150px;height:50px">Read More</a>

<!-- HOW WE PRICE -->
<h2 class="section-title" style="top:2090px"><b>HOW WE</b> PRICE</h2>
<div class="abs price-photo" role="img" aria-label="Technician in hard hat inspecting a water-stained ceiling"></div>

<div class="feature left" style="left:145px;top:2227px">
  <span class="ico ico-navy"><svg width="26" height="30" viewBox="0 0 26 30"><path d="M3 2h13l7 7v19H3z M16 2v7h7" stroke="#fff" stroke-width="2.5" fill="none" stroke-linejoin="round"/></svg></span>
  <h3>Regulatory watch</h3><p>Sed ut perspiciatis unde omnis iste natus error sit voluptatem</p>
</div>
<div class="feature left" style="left:145px;top:2355px">
  <span class="ico ico-blue"><svg width="30" height="30" viewBox="0 0 24 24"><path fill="#fff" d="M6.6 10.8a15.1 15.1 0 0 0 6.6 6.6l2.2-2.2c.3-.3.7-.4 1-.2 1.1.4 2.3.6 3.6.6.6 0 1 .4 1 1V20c0 .6-.4 1-1 1A17 17 0 0 1 3 4c0-.6.4-1 1-1h3.5c.6 0 1 .4 1 1 0 1.3.2 2.5.6 3.6.1.3 0 .7-.2 1z"/></svg></span>
  <h3>Customs advice</h3><p>Sed ut perspiciatis unde omnis iste natus error sit voluptatem</p>
</div>
<div class="feature left" style="left:145px;top:2483px">
  <span class="ico ico-navy"><svg width="30" height="30" viewBox="0 0 24 24"><path fill="#fff" d="M3 17.3V21h3.7L17.8 9.9l-3.7-3.7zM20.7 7a1 1 0 0 0 0-1.4l-2.3-2.3a1 1 0 0 0-1.4 0l-1.8 1.8 3.7 3.7z"/></svg></span>
  <h3>The Audit</h3><p>Sed ut perspiciatis unde omnis iste natus error sit voluptatem</p>
</div>
<div class="feature right" style="left:725px;top:2227px">
  <span class="ico ico-blue"><svg width="32" height="32" viewBox="0 0 24 24"><path fill="#fff" d="M19.4 13a7.6 7.6 0 0 0 0-2l2.1-1.6-2-3.5-2.5 1a7.3 7.3 0 0 0-1.7-1l-.4-2.7h-4l-.4 2.7c-.6.3-1.2.6-1.7 1l-2.5-1-2 3.5L4.6 11a7.6 7.6 0 0 0 0 2l-2.1 1.6 2 3.5 2.5-1c.5.4 1.1.7 1.7 1l.4 2.7h4l.4-2.7c.6-.3 1.2-.6 1.7-1l2.5 1 2-3.5zM12 15.5a3.5 3.5 0 1 1 0-7 3.5 3.5 0 0 1 0 7z"/></svg></span>
  <h3>Control</h3><p>Sed ut perspiciatis unde omnis iste natus error sit voluptatem</p>
</div>
<div class="feature right" style="left:725px;top:2355px">
  <span class="ico ico-navy"><svg width="34" height="34" viewBox="0 0 24 24"><path d="M4 14v-2a8 8 0 0 1 16 0v2" stroke="#fff" stroke-width="2" fill="none"/><rect x="3" y="13" width="4" height="6" rx="1.5" fill="#fff"/><rect x="17" y="13" width="4" height="6" rx="1.5" fill="#fff"/><path d="M19 19c0 2-2 3-5 3" stroke="#fff" stroke-width="1.6" fill="none"/></svg></span>
  <h3>Support</h3><p>Sed ut perspiciatis unde omnis iste natus error sit voluptatem</p>
</div>
<div class="feature right" style="left:725px;top:2483px">
  <span class="ico ico-blue"><svg width="32" height="34" viewBox="0 0 24 26"><path d="M12 2 3 5.5v6c0 6 4 10.5 9 12.5 5-2 9-6.5 9-12.5v-6z" stroke="#fff" stroke-width="2" fill="none"/><path d="m8 13 3 3 5-6" stroke="#fff" stroke-width="2" fill="none"/></svg></span>
  <h3>Security</h3><p style="width:240px">Sed ut perspiciatis unde omnis iste natus error sit voluptatem</p>
</div>

<!-- CTA -->
<div class="abs cta-panel" role="img" aria-label="Technician working in a water-damaged room, tinted navy"></div>
<h2 class="abs cta-title">WE OFFER SAME &amp; NEXT DAY SERVICE. SCHEDULE YOUR APPOINTMENT NOW!</h2>
<a class="btn btn-blue" style="left:598px;top:2992px;width:150px;height:50px">Contact Us</a>

<!-- REVIEWS -->
<div class="abs reviews-bg" role="img" aria-label="Faded bright bathroom interior background"></div>
<h2 class="section-title" style="top:3290px"><b>CUSTOMER</b> REVIEWS</h2>
<div class="arrow" style="left:65px;top:3456px;width:36px;height:36px"><svg width="12" height="12" viewBox="0 0 14 14"><path d="M9 2 4 7l5 5" stroke="#444" stroke-width="2" fill="none"/></svg></div>
<div class="arrow" style="left:1098px;top:3456px;width:36px;height:36px"><svg width="12" height="12" viewBox="0 0 14 14"><path d="M5 2l5 5-5 5" stroke="#444" stroke-width="2" fill="none"/></svg></div>

<div class="review" style="left:130px">
  <div class="avatar" role="img" aria-label="Customer portrait"></div>
  <q>At vero eos et accusamus et iustodio dignissimos ducimus qui blanditiipraesnt ium voluptatum deleniti atq.</q>
  <div class="who">MARISOL PENHART<i>Financial Services Professional</i></div>
  <div class="stars"><svg width="96" height="16" viewBox="0 0 96 16"><g fill="#f3c21b"><path id="s" d="M8 0l2.4 5 5.4.7-4 3.8 1 5.4L8 12.3 3.2 14.9l1-5.4-4-3.8L5.6 5z"/><use href="#s" x="20"/><use href="#s" x="40"/><use href="#s" x="60"/></g><use href="#s" x="80" fill="none" stroke="#f3c21b"/></svg></div>
</div>
<div class="review" style="left:457px">
  <div class="avatar" role="img" aria-label="Customer portrait"></div>
  <q>At vero eos et accusamus et iustodio dignissimos ducimus qui blanditiipraesnt ium voluptatum deleniti atq.</q>
  <div class="who">TOBIAS R. LINDQVIST<i>National Urban Fellow at the Houston</i></div>
  <div class="stars"><svg width="96" height="16" viewBox="0 0 96 16"><g fill="#f3c21b"><use href="#s"/><use href="#s" x="20"/><use href="#s" x="40"/><use href="#s" x="60"/><use href="#s" x="80" opacity=".5"/></g></svg></div>
</div>
<div class="review" style="left:780px">
  <div class="avatar" role="img" aria-label="Customer portrait"></div>
  <q>At vero eos et accusamus et iustodio dignissimos ducimus qui blanditiipraesnt ium voluptatum deleniti atq.</q>
  <div class="who">GRETA HOLLOWAY<i>Creative Strategist | Entrepreneur &amp; Upcoming</i></div>
  <div class="stars"><svg width="96" height="16" viewBox="0 0 96 16"><g fill="#f3c21b"><use href="#s"/><use href="#s" x="20"/><use href="#s" x="40"/><use href="#s" x="60"/></g><use href="#s" x="80" fill="none" stroke="#f3c21b"/></svg></div>
</div>
<a class="btn btn-blue" style="left:428px;top:3647px;width:344px;height:52px">Read More Customer Reviews</a>

<!-- FOOTER -->
<div class="abs footer"></div>
<svg class="abs" style="left:0;top:3770px" width="1200" height="120" viewBox="0 0 1200 120">
  <path d="M0 95 C250 40 500 20 750 30 C950 38 1100 60 1200 40 L1200 120 L0 120Z" fill="#1d222b"/>
  <path d="M0 80 C250 25 500 5 750 15 C950 23 1100 45 1200 25 L1200 40 C1100 60 950 38 750 30 C500 20 250 40 0 95Z" fill="#1c2b4a"/>
</svg>

<div class="contact" style="top:3962px"><span class="ico"><svg width="14" height="18" viewBox="0 0 14 18"><path d="M7 0a7 7 0 0 0-7 7c0 5 7 11 7 11s7-6 7-11a7 7 0 0 0-7-7zm0 9.5A2.5 2.5 0 1 1 7 4.5a2.5 2.5 0 0 1 0 5z" fill="#fff"/></svg></span><span>314,At vero eos et accu<br>samus et iusto odio dimos ducimu</span></div>
<div class="contact" style="top:4032px"><span class="ico fill"><svg width="18" height="18" viewBox="0 0 24 24"><path fill="#fff" d="M6.6 10.8a15.1 15.1 0 0 0 6.6 6.6l2.2-2.2c.3-.3.7-.4 1-.2 1.1.4 2.3.6 3.6.6.6 0 1 .4 1 1V20c0 .6-.4 1-1 1A17 17 0 0 1 3 4c0-.6.4-1 1-1h3.5c.6 0 1 .4 1 1 0 1.3.2 2.5.6 3.6.1.3 0 .7-.2 1z"/></svg></span><span>+1 888 888 8888</span></div>
<div class="contact" style="top:4092px"><span class="ico"><svg width="18" height="14" viewBox="0 0 18 14"><rect x="0.5" y="0.5" width="17" height="13" rx="2" fill="#fff"/><path d="M1 1.5 9 8l8-6.5" stroke="#1d222b" stroke-width="1.6" fill="none"/></svg></span><span>info@kelvornllc.com</span></div>

<div class="abs links">
  <h4>QUICK LINKS</h4>
  <ul><li>Home</li><li>About us</li><li>Services</li><li>Reviews</li><li>News</li><li>Contact us</li></ul>
</div>
<div class="abs footer-brand">KELVORN<small>LLC</small></div>
<p class="abs legal">© 2022 Kelvorn LLC. All rights reserved &nbsp;|&nbsp; Privacy &nbsp;|&nbsp; Terms of Use</p>

</body>
</html>
```